Premium Business Card for Wealth Creation

Please see attached business card for example.
Happy to look at options like Blue background with Yellow
Target Market(s)
People who want to buy investment property or create wealth
Industry/Entity Type
Investment
Contact Information for Business Card
Tel: 1800 514 973
Mobile: 0417 295 641
Address: Level 1, 74 Carrow Lane Brighton Vic 3186
Name: Malcolm Perrett
Title: CEO
Website: www.velmora.com.au
Email: malcolm@velmora.com.au
Font styles to use
Sans Serif
Colors
0255a3
fbed22
Requirements
Must have
- Look great

```html
<!DOCTYPE html>
<html lang="en">
<head>
<meta charset="utf-8">
<title>Velmora Business Card</title>
<link rel="stylesheet" href="https://fonts.googleapis.com/css2?family=Noto+Sans:wght@400;700;800&display=swap">
<style>
  :root {
    --brand-blue: #3953a4;
    --brand-yellow: #fcd12e;
    --card-white: #ffffff;
    --page-bg: #e8e5e1;
  }
  html, body {
    margin: 0;
    padding: 0;
    width: 1200px;
    height: 902px;
    overflow: hidden;
    background: var(--page-bg);
    font-family: "Noto Sans", Arial, sans-serif;
  }
  .business-card {
    position: absolute;
    left: 80px;
    top: 154px;
    width: 1040px;
    height: 594px;
    background: var(--card-white);
    overflow: hidden;
    box-shadow: 0 6px 24px rgba(0, 0, 0, 0.18);
  }
  .card-swoosh {
    position: absolute;
    inset: 0;
    width: 100%;
    height: 100%;
  }
  .brand {
    position: absolute;
    left: 52px;
    top: 93px;
    display: flex;
    align-items: center;
    gap: 22px;
  }
  .brand-dot {
    width: 108px;
    height: 108px;
    border-radius: 50%;
    background: var(--brand-yellow);
  }
  .brand-name {
    font-size: 80px;
    font-weight: 800;
    color: var(--brand-blue);
    letter-spacing: 6px;
    line-height: 1;
  }
  .contact-block {
    position: absolute;
    left: 49px;
    top: 262px;
    color: var(--brand-blue);
  }
  .person-name {
    margin: 0;
    font-size: 35px;
    font-weight: 700;
    line-height: 40px;
  }
  .person-title {
    margin: 0 0 20px;
    font-size: 26px;
    font-weight: 400;
    color: var(--brand-yellow);
    line-height: 30px;
  }
  .address {
    margin: 0 0 12px;
    font-style: normal;
    font-size: 26px;
    line-height: 34px;
  }
  .contact-list {
    list-style: none;
    margin: 0;
    padding: 0;
    font-size: 26px;
    line-height: 33px;
  }
  .contact-list li {
    display: flex;
    align-items: center;
    gap: 8px;
  }
  .contact-icon {
    width: 25px;
    height: 25px;
    flex: none;
  }
</style>
</head>
<body>
  <main class="business-card">
    <svg class="card-swoosh" viewBox="0 0 941 537" preserveAspectRatio="none" aria-hidden="true">
      <path fill="var(--brand-yellow)"
        d="M292 0 L420 0 C690 55 855 170 838 330 C826 420 765 490 682 537 L672 537 C742 490 814 420 824 330 C840 180 620 40 292 0 Z"/>
      <path fill="var(--brand-blue)"
        d="M582 0 C760 60 880 170 852 330 C835 420 770 490 690 537 L941 537 L941 0 Z"/>
    </svg>

    <div class="brand">
      <span class="brand-dot"></span>
      <span class="brand-name">VELMORA</span>
    </div>

    <section class="contact-block">
      <h1 class="person-name">Malcolm Perrett</h1>
      <p class="person-title">CEO</p>
      <address class="address">Level 1, 74 Carrow Lane<br>Larkfield Vic 3190</address>
      <ul class="contact-list">
        <li>
          <svg class="contact-icon" viewBox="0 0 24 24" aria-label="Telephone">
            <rect width="24" height="24" fill="var(--brand-yellow)"/>
            <path fill="#fff" d="M5 9 C5 6 19 6 19 9 L16 10 L15 8 L9 8 L8 10 Z M7 12 L17 12 L18 18 L6 18 Z"/>
          </svg>
          1800 514 973
        </li>
        <li>
          <svg class="contact-icon" viewBox="0 0 24 24" aria-label="Mobile">
            <rect width="24" height="24" fill="var(--brand-yellow)"/>
            <rect x="8" y="4" width="8" height="16" rx="1.5" fill="none" stroke="#fff" stroke-width="1.6"/>
            <rect x="9.6" y="6" width="4.8" height="7" fill="#fff"/>
          </svg>
          0417 295 641
        </li>
        <li>
          <svg class="contact-icon" viewBox="0 0 24 24" aria-label="Email">
            <rect width="24" height="24" fill="var(--brand-yellow)"/>
            <rect x="4" y="7" width="16" height="11" fill="none" stroke="#fff" stroke-width="1.6"/>
            <path d="M4 7 L12 13 L20 7" fill="none" stroke="#fff" stroke-width="1.6"/>
          </svg>
          malcolm@velmora.com.au
        </li>
        <li>
          <svg class="contact-icon" viewBox="0 0 24 24" aria-label="Website">
            <rect width="24" height="24" fill="var(--brand-yellow)"/>
            <circle cx="12" cy="12" r="7.5" fill="none" stroke="#fff" stroke-width="1.5"/>
            <ellipse cx="12" cy="12" rx="3.2" ry="7.5" fill="none" stroke="#fff" stroke-width="1.3"/>
            <path d="M4.5 12 H19.5 M6 8 H18 M6 16 H18" stroke="#fff" stroke-width="1.2"/>
          </svg>
          www.velmora.com.au
        </li>
      </ul>
    </section>
  </main>
</body>
</html>
```